plumrivet-loans.com

We are a small dollar lending company that will revolutionize the industry. We will do this by being completely transparent, fee free, etc and an interest rate that normal people can afford to pay. Over 10X less than our competition. We only allow our members to pay bills " bills paid fast", within 72 hours. Payday loans typically charge from 390%-600% with a terrible payback structure. We charge 36%, period, with a payback structure over 12 months. Our site will be very simple and easy to use but elegant at the same time. We do not want the site to be too busy, less is more and easier. We will have; Home, The Story, Why Plumrivet.com, Are you eligible? Members, Clients. To become a member you have to be referred by a current client of Plumrivet.com. A lot of the busy stuff will be saved for the Members and Clients sections. The feel must be elegant, easy to use and very simple to understand. I am looking for the green, white and black combinations of colors, very similar to my logo that was designed by ArtHively.

```html
<!DOCTYPE html>
<html lang="en">
<head>
<meta charset="utf-8">
<title>Plumrivet — Peace of Mind</title>
<link rel="stylesheet" href="https://fonts.googleapis.com/css2?family=Arvo:wght@700&family=Signika:wght@300;400;600&family=Arimo:wght@400&display=swap">
<style>
  :root {
    --green: #86bd3d;
    --black: #111111;
    --ink: #333333;
    --white: #ffffff;
    --panel: #efefef;
    --hero-top: #cdbfb4;
    --hero-mid: #8a8ea8;
    --hero-bottom: #5f6b8c;
  }
  * { margin: 0; padding: 0; box-sizing: border-box; }
  html, body { width: 1200px; height: 1117px; overflow: hidden; background: var(--white); }
  body { position: relative; font-family: "Signika", sans-serif; color: var(--ink); }

  .hero {
    position: absolute; left: 0; top: 0; width: 1200px; height: 622px;
    background: linear-gradient(180deg, var(--hero-top) 0%, var(--hero-mid) 50%, var(--hero-bottom) 100%);
  }

  .site-header { position: absolute; left: 0; top: 0; width: 1200px; height: 110px; }
  .brand { position: absolute; left: 52px; top: 31px; display: flex; align-items: center; gap: 12px; }
  .brand-mark { width: 66px; height: 66px; background: var(--green); border-radius: 8px; }
  .brand-name { font-weight: 400; font-size: 26px; color: var(--black); }

  .main-nav { position: absolute; left: 318px; top: 53px; display: flex; gap: 33px; }
  .main-nav a { font-size: 15px; font-weight: 600; color: var(--black); text-decoration: none; }

  .owner-login {
    position: absolute; left: 1076px; top: 48px; width: 103px; height: 31px;
    background: var(--black); color: var(--white); font-size: 13.5px; font-weight: 600;
    display: flex; align-items: center; justify-content: center; text-decoration: none;
  }

  .hero-copy { position: absolute; left: 75px; top: 278px; color: var(--white); }
  .hero-title { font-family: "Arvo", serif; font-weight: 700; font-size: 41px; line-height: 46px; }
  .hero-sub { font-weight: 300; font-size: 35px; line-height: 40px; margin-top: 8px; letter-spacing: .5px; }
  .hero-sub strong { font-weight: 600; }

  .card {
    position: absolute; top: 689px; width: 388px; height: 256px;
    background: var(--panel); box-shadow: 0 0 3px rgba(0,0,0,.18);
  }
  .card-left { left: 187px; }
  .card-right { left: 609px; }
  .card-head { height: 93px; background: var(--white); text-align: center; padding-top: 17px; }
  .card-title { font-size: 28px; font-weight: 400; color: var(--green); line-height: 32px; }
  .card-note { font-family: "Arimo", sans-serif; font-size: 17px; color: var(--ink); margin-top: 4px; }

  .contact { text-align: center; font-size: 23px; color: #444; line-height: 25px; padding-top: 42px; }
  .contact strong { font-weight: 600; }

  .client-form { padding-top: 41px; text-align: center; }
  .client-id {
    width: 283px; height: 35px; border: 1px solid #aaa; background: var(--white);
    font-family: "Arimo", sans-serif; font-size: 13px; padding-left: 13px; color: #444; letter-spacing: .5px;
  }
  .client-id::placeholder { color: #444; }
  .submit {
    display: block; margin: 21px auto 0; width: 169px; height: 31px; border: 0; border-radius: 3px;
    background: var(--green); color: var(--white); font-family: "Arimo", sans-serif; font-size: 12px; letter-spacing: .8px;
  }

  .footer-rule { position: absolute; left: 0; top: 1005px; width: 1200px; height: 6px; background: var(--green); }
  .site-footer { position: absolute; left: 0; top: 1016px; width: 1200px; height: 101px; background: var(--green); color: var(--white); }
  .footer-nav { position: absolute; left: 26px; top: 34px; font-size: 15px; font-weight: 300; }
  .footer-nav a { color: var(--white); text-decoration: none; }
  .copyright { position: absolute; left: 26px; top: 61px; font-family: "Arimo", sans-serif; font-size: 12.5px; }
  .social { position: absolute; left: 968px; top: 38px; display: flex; gap: 9px; }
  .social a { width: 33px; height: 33px; border-radius: 5px; background: rgba(255,255,255,.85); display: block; }
</style>
</head>
<body>
  <section class="hero" role="img" aria-label="Photograph of a woman sitting on a rock looking out over the ocean at sunset"></section>

  <header class="site-header">
    <div class="brand"><span class="brand-mark"></span><span class="brand-name">Plumrivet</span></div>
    <nav class="main-nav">
      <a href="#">Home</a><a href="#">The Story</a><a href="#">Why Plumrivet.com</a><a href="#">Are You Eligible?</a><a href="#">Members</a><a href="#">Clients</a>
    </nav>
    <a class="owner-login" href="#">Owner Login</a>
  </header>

  <div class="hero-copy">
    <h1 class="hero-title">Peace of Mind</h1>
    <p class="hero-sub">Bills paid within <strong>72 hours</strong></p>
  </div>

  <section class="card card-left">
    <div class="card-head">
      <h2 class="card-title">Not a Client Yet</h2>
      <p class="card-note">Please Contact</p>
    </div>
    <p class="contact">Phone : <strong>XXX-XXX-XXX</strong><br><strong>or</strong><br>Email : <strong>info@plumrivet-loans.com</strong></p>
  </section>

  <section class="card card-right">
    <div class="card-head">
      <h2 class="card-title">Current Client</h2>
      <p class="card-note">Enter Your Client ID</p>
    </div>
    <form class="client-form">
      <input class="client-id" type="text" placeholder="Enter Here">
      <button class="submit" type="button">SUBMIT</button>
    </form>
  </section>

  <div class="footer-rule"></div>
  <footer class="site-footer">
    <nav class="footer-nav">
      <a href="#">Home</a> | <a href="#">The Story</a> | <a href="#">Why Plumrivet.com</a> | <a href="#">Are You Eligible?</a> | <a href="#">Members</a> | <a href="#">Clients</a>
    </nav>
    <p class="copyright">Copyright (c)2013 by plumrivet-loans.com</p>
    <div class="social">
      <a href="#" aria-label="Social link"></a><a href="#" aria-label="Social link"></a><a href="#" aria-label="Social link"></a><a href="#" aria-label="Social link"></a><a href="#" aria-label="Social link"></a>
    </div>
  </footer>
</body>
</html>
```